Brenvick Holdings LLC, new Business cards

I'm moving offices and need new cards. Plus I'm open to modifying the current design of my card. I will keep the logo but would like to explore other layouts and fonts for the design. I've included the current double sided card for reference. I Like the navy color and white. Might be open to grays or silver. Needs to be clean and elegant.

Target Market(s)

Investors, buyers & sellers of private equities and real estate.

Contact Information for Business Card

Brenvick Holdings
Dorian P.K. Halvers, Managing Principal
418 Ostrander Ave., Suite 612
Denver, CO 80319
M: 970-555-0147, O: 303-555-0192
Dorian@brenvickholdings.example
Brenvickholdings.example

Colors
0354a2
ffffff
c4c4c4

Requirements
Must have
• Business card details.
• Logo raised or embossed, it was designed after a wax seal. Current has raised ink.
Nice to have
• Space on card to write additional notes.

```html
<!DOCTYPE html>
<html lang="en">
<head>
<meta charset="utf-8">
<title>Brenvick Holdings – Business Card</title>
<link href="https://fonts.googleapis.com/css2?family=Source+Sans+3:wght@400;600;700&display=swap" rel="stylesheet">
<style>
  :root {
    --navy: #0354a2;
    --navy-tone: #1a64b0;
    --white: #ffffff;
    --silver: #c4c4c4;
    --ink: #5a5a5a;
    --backdrop: #ececec;
  }
  * { box-sizing: border-box; margin: 0; padding: 0; }
  html, body {
    width: 1200px; height: 1200px; overflow: hidden;
    background: var(--backdrop);
    font-family: "Source Sans 3", Arial, sans-serif;
  }
  .card {
    position: absolute; left: 250px;
    width: 700px; height: 400px;
  }
  .card-front { top: 160px; background: var(--navy); }
  .card-back { top: 640px; background: var(--white); }

  .brand {
    position: absolute; display: flex; flex-direction: column;
    align-items: center; text-align: center; gap: 14px;
  }
  .brand-dot { width: 70px; height: 70px; border-radius: 50%; }
  .brand-name {
    font-weight: 700; font-size: 30px; line-height: 1.05;
    letter-spacing: 0.12em; text-transform: uppercase;
  }
  .card-front .brand { left: 0; right: 0; top: 118px; }
  .card-front .brand-dot { background: var(--navy-tone); }
  .card-front .brand-name { color: var(--navy-tone); }

  .card-back .brand { left: 40px; width: 300px; top: 118px; }
  .card-back .brand-dot { background: var(--navy); }
  .card-back .brand-name { color: var(--navy); }

  .divider {
    position: absolute; left: 362px; top: 70px; width: 1px; height: 270px;
    background: var(--silver);
  }
  .details {
    position: absolute; left: 392px; top: 78px; right: 20px;
    color: var(--ink); font-size: 17px; line-height: 1.3;
  }
  .person-name { color: var(--navy); font-weight: 700; font-size: 25px; line-height: 1.1; }
  .person-title { font-size: 18px; margin-bottom: 14px; }
  .address { margin-bottom: 6px; }
  .contact-list { list-style: none; }
  .contact-list li { display: flex; align-items: center; gap: 8px; }
  .contact-list svg { width: 15px; height: 15px; flex: none; }
  .icon-stroke { fill: none; stroke: var(--navy); stroke-width: 1.8; }
  .icon-fill { fill: var(--navy); }
</style>
</head>
<body>

<section class="card card-front" aria-label="Card front">
  <div class="brand">
    <span class="brand-dot"></span>
    <span class="brand-name">Brenvick<br>Holdings</span>
  </div>
</section>

<section class="card card-back" aria-label="Card back">
  <div class="brand">
    <span class="brand-dot"></span>
    <span class="brand-name">Brenvick<br>Holdings</span>
  </div>
  <div class="divider"></div>
  <div class="details">
    <p class="person-name">Dorian P.K. Halvers</p>
    <p class="person-title">Managing Principal</p>
    <p class="address">418 Ostrander Ave., Suite 612<br>Denver, CO 80319</p>
    <ul class="contact-list">
      <li class="contact-mobile">
        <svg viewBox="0 0 16 16" aria-label="Mobile"><rect class="icon-stroke" x="4" y="1" width="8" height="14" rx="1.5"/></svg>
        970.555.0147
      </li>
      <li class="contact-office">
        <svg viewBox="0 0 16 16" aria-label="Office"><path class="icon-fill" d="M3 1.5l3 .5 1 3-2 1.5c1 2 2.5 3.5 4.5 4.5L11 9l3 1 .5 3c-.5 1.5-2 2-3 1.5C6 12.5 3.5 10 1.5 4.5 1 3.5 1.5 2 3 1.5z"/></svg>
        303.555.0192
      </li>
      <li class="contact-email">
        <svg viewBox="0 0 16 16" aria-label="Email"><rect class="icon-stroke" x="1.5" y="3.5" width="13" height="9"/><path class="icon-stroke" d="M1.5 3.5L8 9l6.5-5.5"/></svg>
        dorian@brenvickholdings.example
      </li>
      <li class="contact-web">
        <svg viewBox="0 0 16 16" aria-label="Website"><circle class="icon-stroke" cx="8" cy="8" r="6.5"/><path class="icon-stroke" d="M1.5 8h13M8 1.5c-3 3.5-3 9.5 0 13M8 1.5c3 3.5 3 9.5 0 13"/></svg>
        brenvickholdings.example
      </li>
    </ul>
  </div>
</section>

</body>
</html>
```